Corporate Design für eine Hautarztpraxis gesucht
Die Zusammenarbeit mit TELUVI war geprägt von höchster Professionalität. Als erstes natürlich das Ergebnis, die Aussagekraft und die Anmutung des entworfenen Designs, da wurden die Anforderungen zu 100 % umgesetzt. Top-Kreativer mit Einfühlungsvermögen in den Kundenwunsch. Als zweites die Zusammenarbeit; verbindliche Kommunikation, die Designentwürfe wurden von TELUVI erklärt und er scheut nicht davor zurück, mitzuteilen wenn die Änderungswünsche vom Briefing und seiner Vorstellung der Umsetzung abweichen, prompte Reaktion auf Kommentare Als drittes die Zuverlässigkeit; alle Zusagen wurden eingehalten, auch das Feintuning nach Projektende war vorbildlich. Zusammenfassend: Top Designer, Vollprofi und 100% Zufriedenheit, danke und jederzeit gerne wieder!!! Working with TELUVI in the project was highly professional. First of all the result and the appearance of the logo and the printproducts; the job fullfillment has reached 100%. TELUVI is a top-creative with understanding and feeling for customer needs. Secondly working with him; the drafts were explained, communication to the point and fast responses to the remarks, and he was free in telling his opinion, if the remarks would lead in the wrong direction Third the reliability; everything was delivered, nothing missed, also the work and finetuning after the official end of the project was to our full satisfaction. Conclusion: Top designer, a real pro, 100 % satisfaction, thanks a lot and we would do it always again!!!
Zielgruppe
Neugründung einer Hautarztpraxis (Gemeinschaftspraxis) von drei Ärzten/Innen
Angeboten wird ein umfassendes medizinisches Spektrum für Kassen- und Privatpatienten sowie Dienstleistungen im Bereich Dermatologischer Kosmetik (Anti Aging, Lasertherapie, Botox, ...)
Die Zielgruppe besteht also zum einen Teil aus Patienten mit gesundheitlichen Problemen der Haut und Allergien sowie andererseits aus Kunden die kosmetische Dienstleistungen nachfragen.
Aufgabenstellung
In Bezug auf die Gestaltung sind wir sehr offen und haben noch keine konkrete Vorstellung, freuen uns aber über viele kreative Vorschläge, von denen wir uns den initialen Impuls für das Design des zukünftigen Logos erhoffen, welches dann im Projekt entwickelt werden soll.
Das Logo soll auf jeden Fall aus einer Wort- und Bildmarke bestehen (Prio 1), eventuell in ein Wappen/Emblem eingebunden sein (Prio 2).
Die Haut als menschliches Organ hat vielschichtige Funktionen, sie schützt den Organismus vor äußeren Umwelteinflüssen und repräsentiert den Menschen nach außen.
Die Haut steht auch für Sensibilität, Reinheit und Schönheit, diese Attribute könnten sich im Logo wiederfinden.
Das Logo soll Kompetenz, Seriosität, Eleganz und Sympathie ausstrahlen, dem Kunden Vertrauen vermitteln und im Verhältnis zur Wortmarke gleich stark sein, so dass z.B. bei der Visitenkarte und dem Briefpapier die Anordnung der Wort- zur Bildmarke unterschiedlich gestaltet werden kann.
Feedback können wir erst in den Abendstunden geben, da tagsüber gearbeitet werden muss und das aktuell noch in unterschiedlichen Arztpraxen.

```html
<!DOCTYPE html>
<html lang="de">
<head>
<meta charset="utf-8">
<title>Die Hautmeister – Visitenkarte</title>
<link rel="stylesheet" href="https://fonts.googleapis.com/css2?family=Jost:ital,wght@0,400;1,400&family=Oswald:wght@400&display=swap">
<style>
  :root {
    --ink: #252525;
    --paper: #ffffff;
    --muted: #7a7a7a;
    --soft: #bdbdbd;
    --accent: #e0505a;
  }
  * { margin: 0; padding: 0; box-sizing: border-box; }
  html, body { width: 1067px; height: 1200px; overflow: hidden; background: var(--ink); }
  .sheet { position: relative; width: 1067px; height: 1200px; background: var(--ink); }

  .card-front { position: absolute; left: 0; top: 0; width: 1067px; height: 596px; }
  .divider { position: absolute; left: 0; top: 596px; width: 1067px; height: 7px; background: var(--paper); }
  .front-mark { position: absolute; left: 503px; top: 238px; }
  .front-name {
    position: absolute; left: 0; right: 0; top: 377px;
    text-align: center;
    font-family: "Jost", sans-serif; font-size: 22px; font-weight: 400;
    letter-spacing: 0.45em; padding-left: 0.45em;
    color: var(--muted);
  }

  .card-back {
    position: absolute; left: 12px; top: 613px; width: 1043px; height: 579px;
    border: 5px solid var(--paper);
  }
  .back-name {
    position: absolute; left: 0; right: 0; top: 110px;
    text-align: center;
    font-family: "Oswald", sans-serif; font-size: 48px; font-weight: 400;
    letter-spacing: 0.36em; padding-left: 0.36em;
    color: var(--paper);
  }
  .rule { position: absolute; left: 501px; top: 281px; width: 31px; height: 4px; background: var(--paper); }
  .contact {
    position: absolute; left: 0; right: 0; top: 352px;
    text-align: center;
    font-family: "Jost", sans-serif; font-style: italic; font-size: 16px;
    letter-spacing: 0.5em; padding-left: 0.5em;
    line-height: 30.5px; color: var(--soft);
  }
  .hours {
    position: absolute; left: 0; right: 0; top: 452px;
    text-align: center; white-space: pre;
    font-family: "Jost", sans-serif; font-style: italic; font-size: 16px;
    letter-spacing: 0.5em; padding-left: 0.5em;
    line-height: 29.5px; color: var(--accent);
  }
</style>
</head>
<body>
<main class="sheet">
  <section class="card-front">
    <svg class="front-mark" width="60" height="60" viewBox="0 0 60 60" aria-hidden="true">
      <circle cx="30" cy="30" r="27" fill="none" stroke="#ffffff" stroke-width="3"/>
    </svg>
    <p class="front-name">DIE HAUTMEISTER</p>
  </section>

  <div class="divider"></div>

  <section class="card-back">
    <h1 class="back-name">DIE HAUTMEISTER</h1>
    <div class="rule"></div>
    <address class="contact">
      BIRKENALLEE 40, 79104 FREIBURG<br>
      TELEFON: 0761/5550123<br>
      E-MAIL: POST@HAUTPOST.DE
    </address>
    <p class="hours">MO   8-18 UHR
DI-FR   8-16 UHR</p>
  </section>
</main>
</body>
</html>
```